Brightfold

New company offering Accounting and bookkeeping for small and medium business in Cayman Islands. please see content on my website. www.brightfold.ky or www.brightfold-accountants.co.uk

Industry/Entity Type

Accounting

Requirements
Must have
• Simple, clean design
Should not have
• clutter

```html
<!DOCTYPE html>
<html lang="en">
<head>
<meta charset="utf-8">
<title>Brightfold Accountants</title>
<link href="https://fonts.googleapis.com/css2?family=Open+Sans:wght@400;600;700&family=Roboto+Condensed:wght@700&display=swap" rel="stylesheet">
<style>
:root{
  --blue:#1d8ad0;
  --navy:#0e2a48;
  --text:#4b5563;
  --panel:#eef2f6;
  --badge:#d9dee4;
  --white:#ffffff;
}
*{margin:0;padding:0;box-sizing:border-box}
html,body{width:857px;height:1200px;overflow:hidden;background:var(--white)}
body{font-family:"Open Sans",sans-serif;color:var(--text)}
.flyer{position:relative;width:857px;height:1200px;background:var(--white)}
.masthead{position:absolute;top:0;left:0;width:857px;height:110px;background:var(--white)}
.brand{position:absolute;left:40px;top:26px;display:flex;align-items:center;gap:14px}
.brand-mark{width:58px;height:58px;border-radius:50%;background:var(--blue)}
.brand-name{font-weight:700;font-size:30px;line-height:1.05;color:var(--blue);text-transform:uppercase;letter-spacing:1px}
.partner-badge{position:absolute;right:20px;top:14px;width:90px;height:86px;background:var(--badge);border-radius:4px}
.hero{position:absolute;top:110px;left:0;width:857px;height:350px}
.hero-photo{position:absolute;inset:0;background:linear-gradient(100deg,#0b2340 0%,#15406a 45%,#2a6aa0 75%,#6ea7d2 100%)}
.hero-bar{position:absolute;left:28px;top:58px;width:6px;height:236px;background:var(--blue)}
.hero-title{position:absolute;left:44px;top:50px;font-family:"Roboto Condensed",sans-serif;font-weight:700;font-size:56px;line-height:1.15;color:var(--white);text-transform:uppercase}
.content{position:absolute;top:460px;left:0;width:857px;height:480px;display:flex;padding:34px 40px 0 28px}
.about{width:400px;margin-right:40px}
.services{flex:1}
.section-title{font-weight:700;font-size:22px;color:var(--blue);text-transform:uppercase;margin-bottom:14px}
.about-item{display:flex;gap:10px;font-size:14.5px;line-height:1.5;margin-bottom:14px}
.about-item svg{flex:0 0 16px;margin-top:3px}
.service{display:flex;align-items:center;gap:16px;margin-bottom:24px}
.service-icon{width:52px;height:52px;background:var(--blue);border-radius:4px;display:flex;align-items:center;justify-content:center}
.service-name{font-size:19px;color:var(--blue);text-transform:uppercase;line-height:1.2}
.service-note{font-size:13px;color:var(--text)}
.why{position:absolute;top:945px;left:0;width:857px;height:170px;background:var(--panel);padding:22px 28px}
.why-title{font-weight:700;font-size:30px;color:var(--navy);margin-bottom:10px}
.why-text{font-size:14.5px;line-height:1.55;color:var(--text)}
.contact-bar{position:absolute;top:1115px;left:0;width:857px;height:85px;background:var(--white);border-top:4px solid var(--blue);display:flex;align-items:center;justify-content:space-between;padding:0 24px}
.contact{display:flex;align-items:center;gap:8px;font-size:12.5px;color:var(--navy)}
.contact-icon{width:28px;height:28px;border-radius:50%;background:var(--navy);display:flex;align-items:center;justify-content:center}
</style>
</head>
<body>
<div class="flyer">
  <header class="masthead">
    <div class="brand">
      <div class="brand-mark"></div>
      <div class="brand-name">Brightfold<br>Accountants</div>
    </div>
    <div class="partner-badge"></div>
  </header>

  <section class="hero">
    <div class="hero-photo" role="img" aria-label="Businessman in a suit touching a glowing financial growth chart on a blue background"></div>
    <div class="hero-bar"></div>
    <h1 class="hero-title">Your<br>partner for<br>successful<br>growth</h1>
  </section>

  <section class="content">
    <div class="about">
      <h2 class="section-title">About Us</h2>
      <p class="about-item"><svg width="16" height="16" viewBox="0 0 16 16"><circle cx="8" cy="8" r="8" fill="#1d8ad0"/><path d="M6 4.5L9.5 8L6 11.5" stroke="#fff" stroke-width="2" fill="none"/></svg><span>We are a bookkeeping and accounting service provider based in the Cayman Islands. Offering all-inclusive outsourcing packages at a fixed monthly fee to small and medium businesses who wish to run their business without the stress of accounting paperwork and regulations.</span></p>
      <p class="about-item"><svg width="16" height="16" viewBox="0 0 16 16"><circle cx="8" cy="8" r="8" fill="#1d8ad0"/><path d="M6 4.5L9.5 8L6 11.5" stroke="#fff" stroke-width="2" fill="none"/></svg><span>Our team of qualified accountants are members of the Meridian Society of Ledger Accountants. We are also members of the Ledgerline Cloud Partner Scheme and hold the Tallyway Online Adviser Certificate, ensuring that we are up to date on all the latest developments.</span></p>
    </div>
    <div class="services">
      <h2 class="section-title">Our Services</h2>
      <div class="service">
        <div class="service-icon"><svg width="28" height="30" viewBox="0 0 28 30"><rect x="3" y="1" width="22" height="28" rx="2" fill="none" stroke="#fff" stroke-width="2"/><rect x="7" y="5" width="14" height="6" fill="#fff"/><g fill="#fff"><rect x="7" y="14" width="4" height="3"/><rect x="12" y="14" width="4" height="3"/><rect x="17" y="14" width="4" height="3"/><rect x="7" y="19" width="4" height="3"/><rect x="12" y="19" width="4" height="3"/><rect x="17" y="19" width="4" height="7"/><rect x="7" y="23" width="4" height="3"/><rect x="12" y="23" width="4" height="3"/></g></svg></div>
        <div><div class="service-name">Bookkeeping</div><div class="service-note">Maintaining all your Accounting</div></div>
      </div>
      <div class="service">
        <div class="service-icon"><svg width="30" height="28" viewBox="0 0 30 28"><g fill="#fff"><rect x="3" y="16" width="5" height="10"/><rect x="11" y="11" width="5" height="15"/><rect x="19" y="6" width="5" height="20"/></g><path d="M2 12L10 5L16 8L27 1" stroke="#fff" stroke-width="2" fill="none"/></svg></div>
        <div><div class="service-name">Management Accounts</div><div class="service-note">Key business information</div></div>
      </div>
      <div class="service">
        <div class="service-icon"><svg width="32" height="22" viewBox="0 0 32 22"><rect x="1" y="1" width="30" height="20" rx="2" fill="none" stroke="#fff" stroke-width="2"/><circle cx="16" cy="11" r="5" fill="none" stroke="#fff" stroke-width="2"/><circle cx="6" cy="11" r="1.5" fill="#fff"/><circle cx="26" cy="11" r="1.5" fill="#fff"/></svg></div>
        <div><div class="service-name">Payroll</div><div class="service-note">All you need to pay your staff</div></div>
      </div>
      <div class="service">
        <div class="service-icon"><svg width="32" height="22" viewBox="0 0 32 22"><path d="M2 8L9 2L16 7L23 2L30 8L16 20Z" fill="none" stroke="#fff" stroke-width="2" stroke-linejoin="round"/><path d="M10 10L16 15L22 10" stroke="#fff" stroke-width="2" fill="none"/></svg></div>
        <div><div class="service-name">Other Services</div></div>
      </div>
    </div>
  </section>

  <section class="why">
    <h2 class="why-title">Why Brightfold Accountants?</h2>
    <p class="why-text">We want our clients to feel confident that their bookkeeping system accurately reflects their current situation so they can concentrate on running their business. Our Mission is to provide a professional, reliable and affordable, accounting service, producing meaningful monthly reports to help our clients better understand the numbers in their business and achieve overall success.</p>
  </section>

  <footer class="contact-bar">
    <div class="contact"><span class="contact-icon"><svg width="14" height="14" viewBox="0 0 14 14"><path d="M3 1L5.5 3.5L4 5.5Q5.5 8.5 8.5 10L10.5 8.5L13 11L11 13Q5 12.5 1 3Z" fill="#fff"/></svg></span>(345) 555 0148</div>
    <div class="contact"><span class="contact-icon"><svg width="12" height="15" viewBox="0 0 12 15"><path d="M6 14C6 14 1 8.5 1 5.5A5 5 0 0 1 11 5.5C11 8.5 6 14 6 14Z" fill="#fff"/><circle cx="6" cy="5.5" r="1.8" fill="#0e2a48"/></svg></span>Harbour Point PO Box 40115 Grand Cayman KY1-1402</div>
    <div class="contact"><span class="contact-icon"><svg width="14" height="10" viewBox="0 0 14 10"><rect x="0.5" y="0.5" width="13" height="9" fill="#fff"/><path d="M0.5 0.5L7 6L13.5 0.5" stroke="#0e2a48" fill="none"/></svg></span>info@brightfold.ky</div>
    <div class="contact"><span class="contact-icon"><svg width="14" height="14" viewBox="0 0 14 14"><circle cx="7" cy="7" r="6" fill="none" stroke="#fff" stroke-width="1.4"/><ellipse cx="7" cy="7" rx="2.6" ry="6" fill="none" stroke="#fff" stroke-width="1.2"/><path d="M1 7H13" stroke="#fff" stroke-width="1.2"/></svg></span>www.brightfold.ky</div>
  </footer>
</div>
</body>
</html>
```